Larkspur Ridge Management - Business Cards

I need business cards. My current logo was designed by a designer at this site and I very much like and am happy with the results. I would like a business card that is trendy, unique, current yet professional. I deal with high net worth clients daily

Target Market(s)

Out of state investors looking to get into the rental market in Ohio

Industry/Entity Type

Property Management, Consulting

Contact Information for Business Card

Name, Title (Chief Financial Officer) office phone number (555) 817-3094 website address larkridgemgmt.example

Font styles to use
Sans Serif

Colors
0054AA
0677BA
7BADD7
CADEEF
E8F1F8
0094D4
00A9DD
6FCCEA
C7EBF8
E9F6FB
00AB8E
00BBA5
67D7C9
C6EFE9
E9F9F6

```html
<!DOCTYPE html>
<html lang="en">
<head>
<meta charset="utf-8">
<title>Larkspur Ridge Management – Business Card</title>
<link rel="stylesheet" href="https://fonts.googleapis.com/css2?family=Montserrat:wght@500;700;800&family=Mulish:wght@400;500&display=swap">
<style>
  :root {
    --canvas: #e9e9e8;
    --card: #fbfbf9;
    --navy: #1f2f5c;
    --red: #c62a30;
    --frame: #c9cacc;
    --rule: #5c6680;
    --pattern-light: #f6f6f4;
    --pattern-dark: #eeeeeb;
  }
  * { box-sizing: border-box; margin: 0; padding: 0; }
  html, body { width: 1200px; height: 1200px; overflow: hidden; }
  body {
    background: var(--canvas);
    position: relative;
    font-family: "Mulish", "Helvetica Neue", Arial, sans-serif;
  }
  .card {
    position: absolute;
    top: 202px;
    width: 446px;
    height: 796px;
    background: var(--card);
  }
  .card--front { left: 117px; overflow: hidden; }
  .card--back { left: 646px; }

  /* Front */
  .front-texture {
    position: absolute;
    inset: 0;
    background: radial-gradient(ellipse at center, var(--pattern-light) 35%, var(--pattern-dark) 100%);
  }
  .brand-name {
    position: absolute;
    left: 0; right: 0;
    top: 520px;
    text-align: center;
    font-family: "Montserrat", Arial, sans-serif;
    font-weight: 800;
    font-size: 40px;
    line-height: 1.05;
    letter-spacing: 0.5px;
    color: var(--navy);
    text-transform: uppercase;
  }
  .brand-rule {
    position: absolute;
    left: 84px;
    width: 276px;
    top: 662px;
    height: 2px;
    background: var(--red);
  }

  /* Back */
  .back-frame {
    position: absolute;
    inset: 18px;
    width: calc(100% - 36px);
    height: calc(100% - 36px);
  }
  .contact {
    position: absolute;
    left: 0; right: 0;
    top: 306px;
    text-align: center;
    color: var(--navy);
  }
  .contact__name {
    font-family: "Montserrat", Arial, sans-serif;
    font-weight: 700;
    font-size: 30px;
    letter-spacing: 0.6px;
    line-height: 38px;
  }
  .contact__title {
    font-family: "Montserrat", Arial, sans-serif;
    font-weight: 500;
    font-size: 21px;
    letter-spacing: 0.3px;
    margin-top: 6px;
    line-height: 26px;
  }
  .contact__divider {
    width: 154px;
    height: 1px;
    background: var(--rule);
    margin: 16px auto 12px;
  }
  .contact__line {
    font-size: 22px;
    font-weight: 500;
    line-height: 28px;
  }
  .card__band {
    position: absolute;
    left: 0; right: 0; bottom: -6px;
    height: 6px;
    background: var(--navy);
  }
</style>
</head>
<body>
  <section class="card card--front" aria-label="Card front">
    <div class="front-texture" role="img" aria-label="Subtle embossed diamond pattern across the card face"></div>
    <p class="brand-name">Larkspur Ridge<br>Management</p>
    <div class="brand-rule"></div>
  </section>

  <section class="card card--back" aria-label="Card back">
    <svg class="back-frame" viewBox="0 0 410 760" preserveAspectRatio="none" aria-hidden="true">
      <g fill="none" stroke="var(--frame)" stroke-width="1.2">
        <rect x="0.6" y="0.6" width="408.8" height="758.8"/>
        <path d="M0.6 30 L30 0.6 M8 30 L8 8 L30 8"/>
        <path d="M409.4 30 L380 0.6 M402 30 L402 8 L380 8"/>
        <path d="M0.6 730 L30 759.4 M8 730 L8 752 L30 752"/>
        <path d="M409.4 730 L380 759.4 M402 730 L402 752 L380 752"/>
      </g>
    </svg>
    <div class="contact">
      <h1 class="contact__name">DANIEL R. HALE</h1>
      <p class="contact__title">CHIEF FINANCIAL OFFICER</p>
      <div class="contact__divider"></div>
      <p class="contact__line">Phone: (555) 817-3094</p>
      <div class="contact__divider"></div>
      <p class="contact__line">Website: larkridgemgmt.example</p>
    </div>
    <div class="card__band"></div>
  </section>
</body>
</html>
```